Promo pages for me as a speaker who has expert advice for educators and as a consultant..

I need a promo page (or two) designed for introducing myself and my services as a speaker. I want to introduce myself to local radio, newspaper, school districts, churches and TV stations as a possible guest. The promo pages have to include my first book, Lanterns over the Schoolyard which is available on Rivvenmart.com and describes my true experience as an inner-city high school teacher. It encapsulates educational strategies which can empower teachers and provide guidelines for greater success in the classroom setting; and consequently, for greater individual student motivation and achievement. My second book, Quiet Notes to Nana (also available on Rivvenmart.com), is a compilation of inspirational true stories to uplift and encourage the reader. Both are Christian based. I want the public (also churches) to be more aware of educators and their difficult work. I want teachers to know there are strategies that work in establishing a better learning environment, especially within our diverse culture and advanced technology influence.

Target Market(s)

local newspapers, radio stations, TV news stations, school districts and churches

Font styles to use
Serif
Sans Serif
Script

Colors

Designer to choose colors to be used in the design.

Requirements
Must have
• Pictures of both books, my website info/link TallMeadowAdvising.com, a picture of me. What I offer: encouragement for teachers, strategies that work for teachers and individuals, families, ministries and businesses. Bullet phrases stating how I can help. I will list the bullet phrases for each promo page to the graphic designer when needed.
Nice to have
• I would like to see two kinds of promo sheets. One with focus on education. Another with focus on Biblical truths as foundation for success in the public workplace.

```html
<!DOCTYPE html>
<html lang="en">
<head>
<meta charset="utf-8">
<title>Dana L. Whitmore – Speaker Promo Sheets</title>
<link rel="stylesheet" href="https://fonts.googleapis.com/css2?family=Alfa+Slab+One&family=Cabin:ital,wght@0,400;0,500;0,600;0,700;1,500;1,600&family=Lobster&display=swap">
<style>
:root{
  --page:#efece6;
  --chalk:#2f3231;
  --chalk-dark:#1f2221;
  --purple:#6b3a8e;
  --purple-deep:#552a78;
  --purple-light:#8a58b3;
  --teal:#8fc0ae;
  --board-green:#1b6a4c;
  --board-green-dark:#0e4a35;
  --lime:#a9e08f;
  --pill:#c6e6b5;
  --crimson:#b8244a;
  --crimson-dark:#9a1b3c;
  --white:#ffffff;
  --ink:#1d1d1d;
  --wood:#b98a5c;
}
*{box-sizing:border-box;margin:0;padding:0}
html,body{width:1200px;height:1200px;overflow:hidden;background:var(--page)}
body{position:relative;font-family:"Cabin",sans-serif;color:var(--white)}
.flyer{position:absolute;top:254px;width:534px;height:692px;overflow:hidden;box-shadow:0 3px 10px rgba(0,0,0,.18)}
.flyer--education{left:46px;background:linear-gradient(180deg,var(--chalk) 0%,var(--chalk-dark) 100%)}
.flyer--faith{left:620px;background:var(--crimson)}
.abs{position:absolute}
.placeholder{position:absolute}

/* education flyer */
.edu-topline{left:0;top:0;width:534px;height:12px;background:var(--teal)}
.edu-banner{left:0;top:0}
.edu-name{left:16px;top:16px;font-family:"Alfa Slab One",serif;font-size:31px;letter-spacing:1.5px;color:#f1eef4;padding-bottom:3px;border-bottom:2px dotted #e9e2f0;width:345px}
.edu-tagline{left:16px;top:62px;font-size:16.5px;font-weight:600;color:var(--white)}
.edu-headline{left:0;width:534px;top:106px;text-align:center;font-family:"Alfa Slab One",serif;font-size:29px;letter-spacing:1.5px;color:#f4f4f2}
.edu-rule{left:66px;top:146px;width:402px;border-top:2px dotted #e8e8e6}
.edu-sub{left:0;width:534px;top:151px;text-align:center;font-size:19px;font-style:italic;font-weight:600;color:var(--lime)}
.edu-intro{left:24px;top:182px;width:490px;font-size:9.8px;line-height:12.5px;text-align:justify;color:#ecedeb}
.edu-board{left:0;top:0}
.edu-pill{left:155px;top:268px;width:224px;height:24px;border-radius:12px;background:var(--pill);color:var(--board-green-dark);font-size:16px;font-weight:500;text-align:center;line-height:24px;box-shadow:0 0 0 2px var(--board-green)}
.bullets{list-style:none;font-size:9.4px;line-height:12.5px;color:#eef5ee}
.bullets li::before{content:"•";margin-right:4px}
.edu-col1,.edu-col2{white-space:nowrap;z-index:2}
.edu-col1{left:44px;top:306px}
.edu-col2{left:304px;top:306px}
.edu-wood{left:0;top:398px;width:534px;height:238px;background:linear-gradient(180deg,#8a6a4a 0%,var(--wood) 45%,#caa37a 100%)}
.edu-book-back{left:116px;top:425px;width:94px;height:178px;background:linear-gradient(160deg,#c9dde0,#8fb0b6)}
.edu-book-front{left:209px;top:402px;width:160px;height:208px;background:linear-gradient(170deg,#e6ecea 0%,#9fc2c8 60%,#6f8f96 100%)}
.edu-photo{left:369px;top:398px;width:165px;height:238px;background:linear-gradient(180deg,#6c5a4c 0%,#c99f86 45%,#2c2a2a 100%)}

.badge{background:var(--white);border-radius:6px;color:var(--ink);padding:6px 10px 0}
.badge-label{display:block;font-size:9.5px;line-height:11px}
.badge-name{display:block;font-size:16.5px;font-weight:700;line-height:20px}
.edu-badge{left:13px;top:479px;width:90px;height:41px}
.edu-badge .badge-name{font-size:14.5px}

.book-tab{height:26px;border-radius:0 13px 13px 0;font-size:13px;line-height:26px;padding-left:22px;color:var(--white)}
.edu-tab{left:0;top:610px;width:140px;background:#262626}
.contact-bar{left:0;width:534px;background:var(--purple);display:flex;justify-content:center;align-items:center;gap:8px;font-size:13.5px;color:var(--white)}
.contact-bar .sep{opacity:.8}
.contact-bar svg{width:12px;height:12px;margin-right:4px;vertical-align:-1px}
.edu-contact{top:636px;height:27px}
.site-bar{left:0;width:534px;text-align:center;font-size:15px;font-weight:700;color:var(--ink)}
.edu-site{top:663px;height:29px;line-height:29px;background:var(--teal)}

/* faith flyer */
.faith-head{left:0;top:0}
.faith-name{left:24px;top:4px;font-family:"Lobster",cursive;font-size:38px;color:var(--ink)}
.faith-tagline{left:21px;top:53px;font-size:12.5px;font-weight:700;color:var(--crimson-dark)}
.faith-stamp{left:365px;top:8px;width:158px;height:86px;border-radius:6px;background:linear-gradient(90deg,rgba(120,20,50,.35) 0%,rgba(214,170,160,.85) 70%)}
.faith-headline{left:0;width:534px;top:100px;text-align:center;font-family:"Lobster",cursive;font-size:34px;color:var(--white)}
.faith-sub{left:0;width:534px;top:143px;text-align:center;font-size:19px;font-style:italic;font-weight:600;color:var(--lime)}
.faith-rule{left:118px;top:170px;width:302px;border-top:2px dotted #f2d9e0}
.faith-intro{left:27px;top:182px;width:488px;font-size:9.8px;line-height:12.5px;text-align:justify;color:#fbe9ee}
.faith-band{left:0;top:0}
.faith-topics-title{left:249px;top:338px;font-family:"Lobster",cursive;font-size:33px;color:var(--white)}
.faith-list{left:352px;top:355px;width:176px;font-size:9.3px;line-height:11.8px}
.faith-list li{padding-left:9px;text-indent:-9px}
.faith-photo{left:0;top:318px;width:196px;height:284px;background:linear-gradient(180deg,#5d4a3e 0%,#c89c84 45%,#8b7a78 100%)}
.faith-book{left:190px;top:420px;width:152px;height:210px;transform:rotate(-9deg);background:linear-gradient(160deg,#efe7dc 0%,#d2b79a 50%,#a9875f 100%)}
.faith-badge{left:366px;top:565px;width:106px;height:52px;padding:9px 12px 0}
.faith-crimson-strip{left:0;top:604px;width:534px;height:30px;background:var(--crimson)}
.faith-tab{left:0;top:602px;width:171px;background:var(--crimson);box-shadow:0 0 0 2px rgba(255,255,255,.9)}
.faith-contact{top:632px;height:26px}
.faith-site{top:656px;height:36px;line-height:32px;background:var(--white)}
</style>
</head>
<body>

<!-- Education-focused promo sheet -->
<section class="flyer flyer--education" aria-label="Education promo sheet">
  <svg class="abs edu-board" width="534" height="692" viewBox="0 0 534 692" aria-hidden="true">
    <defs>
      <linearGradient id="boardGreen" x1="0" y1="0" x2="0" y2="1">
        <stop offset="0" stop-color="#1d7050"/>
        <stop offset="1" stop-color="#0e4a35"/>
      </linearGradient>
    </defs>
    <path d="M0,318 Q267,244 534,322 L534,692 L0,692 Z" fill="#e8efe9"/>
    <path d="M0,322 Q267,248 534,326 L534,692 L0,692 Z" fill="url(#boardGreen)"/>
  </svg>
  <div class="placeholder edu-wood" role="img" aria-label="Wooden classroom floor"></div>

  <div class="abs edu-topline"></div>
  <svg class="abs edu-banner" width="534" height="110" viewBox="0 0 534 110" aria-hidden="true">
    <path d="M0,0 L400,0 L400,12 Q380,72 230,92 Q110,104 0,104 Z" fill="#e4dcef"/>
    <path d="M0,0 L396,0 L396,12 Q376,68 228,88 Q110,100 0,99 Z" fill="var(--purple)"/>
  </svg>
  <h1 class="abs edu-name">Dana L. Whitmore</h1>
  <p class="abs edu-tagline">Author. Teacher. Speaker.</p>

  <h2 class="abs edu-headline">Teaching and Loving It!</h2>
  <div class="abs edu-rule"></div>
  <p class="abs edu-sub">Discovering Your Strengths for Success</p>
  <p class="abs edu-intro">As a late bloomer at the age of 40, I began a new kind of education as I stepped into the massive foyer of the first high school in the heart of Kansas City. Although I obtained a master’s degree in education, I lacked the skills needed for this environment. I was far from perfect, but my on-the-job training created strategies which brought success for my students as well as providing empowerment for me and others. I want teachers to know there are approaches that work in establishing a better learning environment, especially within our diverse culture and advanced technological influence.</p>

  <div class="abs edu-pill">What You Will Learn:</div>
  <ul class="abs bullets edu-col1">
    <li>Lessons on What Not to do in the Classroom</li>
    <li>Teaching the Unreachable Student</li>
    <li>What I Needed to Know, but Didn’t Learn in College</li>
    <li>Choosing the Most Important Thing</li>
    <li>How to Keep Your Blood Pressure in Check</li>
    <li>Building Positive Student Identity</li>
    <li>Investing in Your Students’ Future</li>
  </ul>
  <ul class="abs bullets edu-col2">
    <li>Flexibility Works Wonders</li>
    <li>Classroom Strategies for Student Success</li>
    <li>Handling the Stress of Standardized Testing</li>
    <li>Dealing with Dishonest Students</li>
    <li>Knowing You Made a Difference</li>
    <li>And much more . . .</li>
  </ul>

  <div class="placeholder edu-book-back" role="img" aria-label="Back cover of the book Lanterns over the Schoolyard with author bio"></div>
  <div class="placeholder edu-book-front" role="img" aria-label="Front cover of the book Lanterns over the Schoolyard, inspirational true stories from an inner-city high school teacher"></div>
  <div class="placeholder edu-photo" role="img" aria-label="Portrait photo of Dana L. Whitmore"></div>

  <div class="abs badge edu-badge"><span class="badge-label">Available at</span><span class="badge-name">Rivvenmart</span></div>

  <div class="abs book-tab edu-tab">To Book Dana:</div>
  <div class="abs contact-bar edu-contact">
    <span><svg viewBox="0 0 24 24" fill="currentColor" aria-hidden="true"><path d="M6.6 10.8a15.1 15.1 0 0 0 6.6 6.6l2.2-2.2c.3-.3.7-.4 1-.2 1.1.4 2.3.6 3.6.6.6 0 1 .4 1 1V20c0 .6-.4 1-1 1A17 17 0 0 1 3 4c0-.6.4-1 1-1h3.5c.6 0 1 .4 1 1 0 1.3.2 2.5.6 3.6.1.3 0 .7-.2 1z"/></svg>555.014.2287</span>
    <span class="sep">|</span>
    <span><svg viewBox="0 0 24 24" fill="none" stroke="currentColor" stroke-width="2" aria-hidden="true"><rect x="3" y="5" width="18" height="14" rx="1"/><path d="M3 6l9 7 9-7"/></svg>TallMeadow@postline.net</span>
  </div>
  <div class="abs site-bar edu-site">TallMeadowAdvising.com</div>
</section>

<!-- Faith-focused promo sheet -->
<section class="flyer flyer--faith" aria-label="Faith and workplace promo sheet">
  <svg class="abs faith-band" width="534" height="692" viewBox="0 0 534 692" aria-hidden="true">
    <defs>
      <linearGradient id="bandPurple" x1="0" y1="0" x2="0" y2="1">
        <stop offset="0" stop-color="#8150a6"/>
        <stop offset="1" stop-color="#5b2c7e"/>
      </linearGradient>
    </defs>
    <path d="M0,286 L40,290 L90,284 L150,292 L210,288 L270,296 L330,292 L390,300 L450,296 L534,304 L534,692 L0,692 Z" fill="url(#bandPurple)"/>
    <path d="M0,0 L322,0 L322,82 L300,86 L280,80 L255,88 L230,83 L205,90 L180,84 L150,91 L120,85 L95,92 L70,86 L40,92 L18,87 L0,90 Z" fill="#ffffff"/>
  </svg>
  <div class="placeholder faith-stamp" role="img" aria-label="Postage stamp and postmark decoration"></div>
  <h1 class="abs faith-name">Dana L. Whitmore</h1>
  <p class="abs faith-tagline">Author. Teacher. Minister. Speaker. Consultant.</p>

  <h2 class="abs faith-headline">Equipped and Empowered!</h2>
  <p class="abs faith-sub">Discovering Your Distinctive Journey</p>
  <div class="abs faith-rule"></div>
  <p class="abs faith-intro">Dana has traveled nationally and internationally as a speaker, teacher and consultant since 2013. As a licensed minister, she has nurtured and supported individuals, couples and other ministries through effective counseling. She is the author of Lanterns over the Schoolyard, which demonstrates God’s faithfulness during her years of teaching and consulting within the inner-city high schools. Quiet Notes to Nana is a compilation of her articles published online. They are inspirational messages of God’s intimate love toward us which encourage and exhort through scripture, stories and Biblical truths. Dana desires that people truly know God’s intense love for them and that they come to realize their identity and empowerment through Christ.</p>

  <div class="abs faith-crimson-strip"></div>
  <div class="placeholder faith-photo" role="img" aria-label="Portrait photo of Dana L. Whitmore"></div>
  <div class="placeholder faith-book" role="img" aria-label="Cover of the book Quiet Notes to Nana, inspirational messages of hope and encouragement"></div>

  <h3 class="abs faith-topics-title">Topics:</h3>
  <ul class="abs bullets faith-list">
    <li>Knowing Your Identity</li>
    <li>Becoming Free from the Past</li>
    <li>Finding Your Journey</li>
    <li>Sustaining Successful Relationships</li>
    <li>Attaining Effective Ministry and Business Strategies</li>
    <li>Empowering Others</li>
    <li>Obtaining and Keeping Unity for Your Team</li>
    <li>Restoring Vision and Purpose</li>
    <li>Implementing a Solid Foundation and Framework</li>
    <li>And much more . . .</li>
  </ul>

  <div class="abs badge faith-badge"><span class="badge-label">Available at</span><span class="badge-name">Rivvenmart</span></div>

  <div class="abs book-tab faith-tab">To Book Dana:</div>
  <div class="abs contact-bar faith-contact">
    <span><svg viewBox="0 0 24 24" fill="currentColor" aria-hidden="true"><path d="M6.6 10.8a15.1 15.1 0 0 0 6.6 6.6l2.2-2.2c.3-.3.7-.4 1-.2 1.1.4 2.3.6 3.6.6.6 0 1 .4 1 1V20c0 .6-.4 1-1 1A17 17 0 0 1 3 4c0-.6.4-1 1-1h3.5c.6 0 1 .4 1 1 0 1.3.2 2.5.6 3.6.1.3 0 .7-.2 1z"/></svg>555.014.2287</span>
    <span class="sep">|</span>
    <span><svg viewBox="0 0 24 24" fill="none" stroke="currentColor" stroke-width="2" aria-hidden="true"><rect x="3" y="5" width="18" height="14" rx="1"/><path d="M3 6l9 7 9-7"/></svg>TallMeadow@postline.net</span>
  </div>
  <div class="abs site-bar faith-site">TallMeadowAdvising.com</div>
</section>

</body>
</html>
```